New Business Card Design*

We are a recruitment company based in Norwich/Cambridge England.
I have included our company logo which we want to remain the same.

What we are looking for is a new creative Business card which will really stand out!!

Contact Information for Business Card

Harriet Vance
email: Harriet@brelvix.co.uk
Address: Tolworth House
Ashgrove Innovation Park
Pelham Road
Norwich
KT9 3QD
Tel:01632 960418

```html
<!DOCTYPE html>
<html lang="en">
<head>
<meta charset="utf-8">
<title>Brelvix Business Card</title>
<link rel="stylesheet" href="https://fonts.googleapis.com/css2?family=Lato:wght@300;400;700&display=swap">
<style>
  :root {
    --page-bg: #e8e6e3;
    --brand-green: #86bf3e;
    --card-grey: #807f86;
    --ink-white: #ffffff;
    --rule-white: rgba(255, 255, 255, 0.9);
    --card-shadow: 0 10px 28px rgba(0, 0, 0, 0.18);
  }
  * { box-sizing: border-box; margin: 0; padding: 0; }
  html, body {
    width: 1200px;
    height: 1200px;
    overflow: hidden;
    background: var(--page-bg);
    font-family: "Lato", sans-serif;
    color: var(--ink-white);
  }
  .canvas {
    position: relative;
    width: 1200px;
    height: 1200px;
  }
  .card {
    position: absolute;
    left: 250px;
    width: 700px;
    height: 400px;
    border-radius: 6px;
    box-shadow: var(--card-shadow);
    overflow: hidden;
  }

  /* Front */
  .card-front {
    top: 150px;
    background: var(--brand-green);
    display: flex;
    align-items: center;
    justify-content: center;
  }
  .front-brand {
    display: flex;
    flex-direction: column;
    align-items: flex-start;
  }
  .front-brand-row {
    display: flex;
    align-items: center;
    gap: 18px;
  }
  .brand-dot {
    display: block;
    border-radius: 50%;
    background: var(--ink-white);
  }
  .front-brand .brand-dot { width: 56px; height: 56px; }
  .front-brand .brand-name {
    font-weight: 700;
    font-size: 72px;
    letter-spacing: -1px;
    line-height: 1;
  }
  .front-brand .brand-tagline {
    margin-left: 76px;
    margin-top: 6px;
    font-size: 13px;
    letter-spacing: 5px;
  }

  /* Back */
  .card-back {
    top: 640px;
    background: var(--card-grey);
  }
  .back-brand-strip {
    position: absolute;
    left: 34px;
    top: 0;
    height: 400px;
    writing-mode: vertical-rl;
    transform: rotate(180deg);
    display: flex;
    flex-direction: row;
    align-items: center;
    justify-content: center;
    gap: 14px;
  }
  .back-brand {
    display: flex;
    flex-direction: column;
    align-items: flex-start;
  }
  .back-brand-row {
    display: flex;
    align-items: center;
    gap: 12px;
  }
  .back-brand .brand-dot { width: 40px; height: 40px; }
  .back-brand .brand-name {
    font-weight: 700;
    font-size: 48px;
    line-height: 1;
  }
  .back-brand .brand-tagline {
    margin-top: 2px;
    margin-right: 52px;
    font-size: 8.5px;
    letter-spacing: 3px;
  }
  .website {
    font-size: 21px;
    letter-spacing: 0.5px;
    font-weight: 400;
  }
  .strip-divider {
    position: absolute;
    left: 188px;
    top: 32px;
    width: 1.5px;
    height: 336px;
    background: var(--rule-white);
  }
  .contact-block {
    position: absolute;
    left: 188px;
    top: 0;
    right: 0;
    bottom: 0;
  }
  .holder-name {
    position: absolute;
    left: 54px;
    top: 52px;
    font-size: 34px;
    font-weight: 400;
  }
  .contact-rule {
    position: absolute;
    left: 0;
    right: 36px;
    height: 1.5px;
    background: var(--rule-white);
  }
  .contact-rule.rule-top { top: 118px; }
  .contact-rule.rule-bottom { top: 240px; }
  .contact-lines {
    position: absolute;
    left: 40px;
    top: 140px;
    list-style: none;
  }
  .contact-lines li {
    display: flex;
    align-items: center;
    gap: 14px;
    font-size: 27px;
    line-height: 38px;
  }
  .contact-icon { width: 20px; height: 20px; flex: none; }
  .address {
    position: absolute;
    left: 40px;
    top: 266px;
    font-style: normal;
    font-size: 20px;
    line-height: 28px;
  }
</style>
</head>
<body>
<main class="canvas">

  <section class="card card-front" aria-label="Business card front">
    <div class="front-brand">
      <div class="front-brand-row">
        <span class="brand-dot"></span>
        <span class="brand-name">Brelvix</span>
      </div>
      <span class="brand-tagline">Technology Recruitment</span>
    </div>
  </section>

  <section class="card card-back" aria-label="Business card back">
    <div class="back-brand-strip">
      <div class="back-brand">
        <div class="back-brand-row">
          <span class="brand-dot"></span>
          <span class="brand-name">Brelvix</span>
        </div>
        <span class="brand-tagline">Technology Recruitment</span>
      </div>
      <span class="website">www.brelvix.co.uk</span>
    </div>

    <div class="strip-divider"></div>

    <div class="contact-block">
      <h1 class="holder-name">Harriet Vance</h1>
      <div class="contact-rule rule-top"></div>
      <ul class="contact-lines">
        <li>
          <svg class="contact-icon" viewBox="0 0 24 24" aria-hidden="true">
            <path fill="#ffffff" d="M6.6 10.8a15.1 15.1 0 0 0 6.6 6.6l2.2-2.2a1 1 0 0 1 1-.25 11.4 11.4 0 0 0 3.6.57 1 1 0 0 1 1 1V20a1 1 0 0 1-1 1A17 17 0 0 1 3 4a1 1 0 0 1 1-1h3.5a1 1 0 0 1 1 1 11.4 11.4 0 0 0 .57 3.6 1 1 0 0 1-.25 1z"/>
          </svg>
          <span>01632 960418</span>
        </li>
        <li>
          <svg class="contact-icon" viewBox="0 0 24 24" aria-hidden="true">
            <rect x="2" y="5" width="20" height="14" fill="#ffffff"/>
            <path d="M2 5l10 8 10-8" fill="none" stroke="#807f86" stroke-width="1.6"/>
          </svg>
          <span>Harriet@brelvix.co.uk</span>
        </li>
      </ul>
      <div class="contact-rule rule-bottom"></div>
      <address class="address">
        Tolworth House, Ashgrove Innovation Park,<br>
        Pelham Road, Norwich, KT9 3QD
      </address>
    </div>
  </section>

</main>
</body>
</html>
```